Creative & Appealing Business Card

Required a business card for Vantrelink
We specialise in claims management services for PPI ( Payment Protection Insurance.
2 sided business card
Round Corners
I like embossed and raised lettering

```html
<!DOCTYPE html>
<html lang="en">
<head>
<meta charset="utf-8">
<title>Vantrelink Business Card</title>
<link href="https://fonts.googleapis.com/css2?family=Open+Sans:ital,wght@0,400;0,700;1,400;1,700&display=swap" rel="stylesheet">
<style>
  :root {
    --backdrop: #b3a693;
    --card-front: #f6f6f5;
    --card-back: #0f1217;
    --ink: #2b2b2b;
    --ink-soft: #4a4a4a;
    --rule: #2a2a2a;
    --blind-press: #222830;
  }
  * { margin: 0; padding: 0; box-sizing: border-box; }
  html, body { width: 1200px; height: 600px; overflow: hidden; }
  body {
    background: var(--backdrop);
    font-family: "Open Sans", Arial, sans-serif;
    position: relative;
  }
  .card {
    position: absolute;
    top: 182px;
    width: 415px;
    height: 236px;
    border-radius: 14px;
  }
  .card--front { left: 120px; background: var(--card-front); color: var(--ink); }
  .card--back { left: 674px; background: var(--card-back); }

  .holder { position: absolute; left: 26px; top: 30px; }
  .holder__name { font-size: 19px; font-weight: 400; font-style: italic; line-height: 1.2; }
  .holder__name strong { font-style: normal; font-weight: 700; }
  .holder__role { font-size: 15px; font-style: italic; color: var(--ink-soft); line-height: 1.3; }

  .brand__name {
    position: absolute;
    font-weight: 700;
    white-space: nowrap;
    letter-spacing: -0.5px;
  }
  .card--front .brand__name {
    right: 40px; top: 34px;
    font-size: 34px;
    color: var(--ink);
  }
  .card--back .brand__name {
    left: 0; right: 0; top: 90px;
    text-align: center;
    font-size: 40px;
    color: var(--blind-press);
  }

  .rules { position: absolute; left: 0; top: 0; }

  .contact { position: absolute; font-size: 12.5px; line-height: 1.35; }
  .contact__label { font-weight: 700; font-style: italic; }
  .contact__value { font-style: italic; color: var(--ink-soft); }
  .contact--phone { left: 22px; top: 145px; }
  .contact--email { left: 220px; top: 145px; }
  .contact--address { left: 22px; top: 188px; }
</style>
</head>
<body>
  <section class="card card--front" aria-label="Card front">
    <div class="holder">
      <p class="holder__name">Alex <strong>Morgan</strong></p>
      <p class="holder__role">Director</p>
    </div>

    <p class="brand__name">Vantrelink</p>

    <svg class="rules" width="415" height="236" viewBox="0 0 415 236" aria-hidden="true">
      <g stroke="#2a2a2a" stroke-width="1.3" fill="#2a2a2a">
        <line x1="14" y1="141" x2="400" y2="141"/>
        <line x1="14" y1="182" x2="400" y2="182"/>
        <line x1="14" y1="223" x2="400" y2="223"/>
        <line x1="208" y1="141" x2="208" y2="182"/>
        <line x1="14" y1="137" x2="14" y2="145"/>
        <line x1="14" y1="219" x2="14" y2="227"/>
        <path d="M400 138 L404 141 L400 144 Z"/>
        <path d="M400 220 L404 223 L400 226 Z"/>
        <circle cx="208" cy="182" r="2"/>
      </g>
    </svg>

    <div class="contact contact--phone">
      <p class="contact__label">Phone.</p>
      <p class="contact__value">+44 100 200 300</p>
    </div>
    <div class="contact contact--email">
      <p class="contact__label">Email.</p>
      <p class="contact__value">alex.morgan@vantrelink.co.uk</p>
    </div>
    <div class="contact contact--address">
      <p class="contact__label">Address.</p>
      <p class="contact__value">Any Lane No.45, Sample Town 67890</p>
    </div>
  </section>

  <section class="card card--back" aria-label="Card back">
    <p class="brand__name">Vantrelink</p>
  </section>
</body>
</html>
```